Kelvaro Video on Demand Slate App UI Design

Kelvaro is part of a VOD(Video On Demand) platform, a close match to our requirement is Brimlane.

We are looking for flat ui design endorsed by quorrel is design guidelines. We have been through the exercise of creating mock ups to guide your thoughts. You don't have to copy the exact concept in mock ups, rather present us with a more creative way of laying out stuff as its dictated in mockups

Along with the screen work we would also like ideas on logo design

You don't have to cover design for all 6 screens attached as long as you can do the main page, detail page and and menu system, you can complete the rest once selected.

Project Deadline Extended
Reason: We have not received enough designs in order to make a decision yet.

Target Market(s)

Video on demand

Industry/Entity Type

Work

Font styles to use
Other font styles liked:
• something that appears very fine on retina devices

Requirements
Must have
• Fully built out screens, with psd files or illustrator files
Nice to have
• have a look at ostrevo tv app, brimlane or tandle movies
Should not have
• no gradients, i have has to be a flat solid color design

```html
<!DOCTYPE html>
<html lang="en">
<head>
<meta charset="utf-8">
<title>Kelvaro – Video on Demand Tablet App</title>
<link rel="stylesheet" href="https://fonts.googleapis.com/css2?family=Roboto:wght@300;400;500&display=swap">
<style>
  :root {
    --page-bg: #dcdcdc;
    --status-bg: #ffffff;
    --status-text: #111111;
    --brand-teal: #00cdb8;
    --tab-teal: #0e8b7d;
    --tab-grey: #8b8e92;
    --tab-grey-text: #55585c;
    --menu-bg: #0b2b2e;
    --menu-active: #071f21;
    --menu-line: #123a3d;
    --menu-text: #6f8f8f;
    --menu-text-active: #e6f1f1;
    --submenu-bg: #081e21;
    --submenu-line: #0f3033;
    --submenu-text: #e8f0f0;
    --content-bg: #222a38;
    --white: #ffffff;
  }

  * { box-sizing: border-box; margin: 0; padding: 0; }

  html, body {
    width: 1200px;
    height: 796px;
    overflow: hidden;
  }

  body {
    background: var(--page-bg);
    font-family: "Roboto", "Helvetica Neue", Arial, sans-serif;
    position: relative;
  }

  .app-screen {
    position: absolute;
    left: 88px;
    top: 14px;
    width: 1024px;
    height: 768px;
    background: var(--content-bg);
    overflow: hidden;
  }

  /* Status bar */
  .status-bar {
    position: absolute;
    left: 0; top: 0;
    width: 100%;
    height: 24px;
    background: var(--status-bg);
    color: var(--status-text);
    font-size: 13px;
    font-weight: 400;
    display: flex;
    align-items: center;
    justify-content: space-between;
    padding: 0 12px;
  }
  .status-left, .status-right { display: flex; align-items: center; gap: 6px; width: 160px; }
  .status-right { justify-content: flex-end; }
  .status-time { font-weight: 500; }
  .battery {
    width: 26px; height: 11px;
    border: 1px solid var(--status-text);
    border-radius: 2px;
    padding: 1px;
    position: relative;
  }
  .battery::after {
    content: "";
    position: absolute;
    right: -3px; top: 3px;
    width: 2px; height: 4px;
    background: var(--status-text);
  }
  .battery-level { display: block; width: 100%; height: 100%; background: var(--status-text); }

  /* Header */
  .app-header {
    position: absolute;
    left: 0; top: 24px;
    width: 100%;
    height: 53px;
    background: var(--brand-teal);
    display: flex;
    align-items: center;
    justify-content: center;
  }
  .menu-toggle { position: absolute; left: 14px; top: 16px; }
  .search-button { position: absolute; right: 16px; top: 17px; }
  .brand {
    display: flex;
    align-items: center;
    gap: 8px;
    color: var(--white);
    font-size: 30px;
    font-weight: 400;
    letter-spacing: -0.5px;
  }
  .brand-mark {
    width: 20px; height: 20px;
    background: var(--white);
  }

  /* Side menu */
  .side-menu {
    position: absolute;
    left: 0; top: 77px;
    width: 262px;
    height: 691px;
    background: var(--menu-bg);
    z-index: 3;
  }
  .menu-list { list-style: none; }
  .menu-item {
    height: 47px;
    display: flex;
    align-items: center;
    gap: 18px;
    padding-left: 18px;
    color: var(--menu-text);
    font-size: 15px;
    font-weight: 300;
    border-bottom: 1px solid var(--menu-line);
  }
  .menu-item svg { width: 18px; height: 18px; flex: none; }
  .menu-item.is-active {
    background: var(--menu-active);
    color: var(--menu-text-active);
    font-weight: 400;
    height: 54px;
  }

  .sub-menu {
    position: absolute;
    left: 262px; top: 77px;
    width: 170px;
    height: 298px;
    background: var(--submenu-bg);
    z-index: 4;
    list-style: none;
  }
  .sub-menu-item {
    height: 47px;
    display: flex;
    align-items: center;
    padding-left: 36px;
    color: var(--submenu-text);
    font-size: 15px;
    font-weight: 300;
    border-bottom: 1px solid var(--submenu-line);
  }
  .sub-menu-item:first-child { height: 54px; }
  .sub-menu-item:last-child { border-bottom: none; }

  /* Tabs */
  .tab {
    position: absolute;
    top: 117px;
    height: 49px;
    display: flex;
    align-items: center;
    justify-content: center;
    font-size: 15px;
    font-weight: 500;
    letter-spacing: 0.5px;
  }
  .tab-popular {
    left: 390px;
    width: 246px;
    background: var(--tab-teal);
    color: var(--menu-text-active);
  }
  .tab-popular::after {
    content: "";
    position: absolute;
    left: 78px;
    bottom: -10px;
    border-left: 10px solid transparent;
    border-right: 10px solid transparent;
    border-top: 10px solid var(--tab-teal);
  }
  .tab-new {
    left: 699px;
    width: 243px;
    background: var(--tab-grey);
    color: var(--tab-grey-text);
  }

  /* Poster grid */
  .poster {
    position: absolute;
    width: 154px;
    height: 154px;
  }
  .poster .play-icon {
    position: absolute;
    left: 53px; top: 53px;
    width: 48px; height: 48px;
  }
  .c1 { left: 262px; } .c2 { left: 433px; } .c3 { left: 608px; } .c4 { left: 785px; }
  .r1 { top: 209px; } .r2 { top: 384px; } .r3 { top: 559px; }
</style>
</head>
<body>
  <main class="app-screen">

    <div class="status-bar">
      <div class="status-left">
        <span>Slate</span>
        <svg width="14" height="11" viewBox="0 0 14 11" aria-hidden="true">
          <path d="M1 4 A9 9 0 0 1 13 4" fill="none" stroke="#111" stroke-width="1.6"/>
          <path d="M3.5 6.5 A5.5 5.5 0 0 1 10.5 6.5" fill="none" stroke="#111" stroke-width="1.6"/>
          <circle cx="7" cy="9.3" r="1.4" fill="#111"/>
        </svg>
      </div>
      <span class="status-time">4:21 PM</span>
      <div class="status-right">
        <span>100%</span>
        <span class="battery"><span class="battery-level"></span></span>
      </div>
    </div>

    <header class="app-header">
      <svg class="menu-toggle" width="24" height="20" viewBox="0 0 24 20" aria-label="Menu">
        <rect x="0" y="1" width="24" height="3" fill="#0b2b2e"/>
        <rect x="0" y="8.5" width="24" height="3" fill="#0b2b2e"/>
        <rect x="0" y="16" width="24" height="3" fill="#0b2b2e"/>
      </svg>
      <div class="brand">
        <span class="brand-mark" aria-hidden="true"></span>
        <span class="brand-name">Kelvaro</span>
      </div>
      <svg class="search-button" width="20" height="20" viewBox="0 0 20 20" aria-label="Search">
        <circle cx="8" cy="8" r="6" fill="none" stroke="#fff" stroke-width="2"/>
        <line x1="12.5" y1="12.5" x2="18" y2="18" stroke="#fff" stroke-width="2.4"/>
      </svg>
    </header>

    <nav class="side-menu">
      <ul class="menu-list">
        <li class="menu-item is-active">
          <svg viewBox="0 0 18 18" aria-hidden="true"><rect x="2" y="3" width="14" height="12" fill="none" stroke="#e6f1f1" stroke-width="1.5"/><path d="M7 6 L12 9 L7 12 Z" fill="#e6f1f1"/></svg>
          Kelvaro TV
        </li>
        <li class="menu-item">
          <svg viewBox="0 0 18 18" aria-hidden="true"><circle cx="6" cy="12" r="3" fill="none" stroke="#6f8f8f" stroke-width="1.4"/><path d="M9 3 A6 6 0 0 1 15 9 M9 6 A3 3 0 0 1 12 9" fill="none" stroke="#6f8f8f" stroke-width="1.4"/></svg>
          Live TV
        </li>
        <li class="menu-item">
          <svg viewBox="0 0 18 18" aria-hidden="true"><rect x="2" y="3" width="14" height="12" fill="none" stroke="#6f8f8f" stroke-width="1.4"/><line x1="5" y1="7" x2="13" y2="7" stroke="#6f8f8f" stroke-width="1.4"/><line x1="5" y1="11" x2="13" y2="11" stroke="#6f8f8f" stroke-width="1.4"/></svg>
          Programme Guide
        </li>
        <li class="menu-item">
          <svg viewBox="0 0 18 18" aria-hidden="true"><path d="M1 3 H4 L6 12 H14 L16 6 H5" fill="none" stroke="#6f8f8f" stroke-width="1.4"/><circle cx="7" cy="15" r="1.3" fill="#6f8f8f"/><circle cx="13" cy="15" r="1.3" fill="#6f8f8f"/></svg>
          Movies Store
        </li>
        <li class="menu-item">
          <svg viewBox="0 0 18 18" aria-hidden="true"><circle cx="9" cy="9" r="5" fill="none" stroke="#6f8f8f" stroke-width="2.6" stroke-dasharray="2.2 1.7"/><circle cx="9" cy="9" r="2" fill="none" stroke="#6f8f8f" stroke-width="1.4"/></svg>
          Settings
        </li>
      </ul>
    </nav>

    <ul class="sub-menu">
      <li class="sub-menu-item">All Channels</li>
      <li class="sub-menu-item">On Air</li>
      <li class="sub-menu-item">Watch Later</li>
      <li class="sub-menu-item">Social</li>
      <li class="sub-menu-item">Favourites</li>
      <li class="sub-menu-item">Recordings</li>
    </ul>

    <div class="tab tab-popular">POPULAR</div>
    <div class="tab tab-new">NEW STARTED</div>

    <section class="poster-grid">
      <div class="poster c2 r1" role="img" aria-label="Movie poster artwork, dark figure in fiery orange tones" style="background:#6e3a18"><svg class="play-icon" viewBox="0 0 48 48" aria-hidden="true"><circle cx="24" cy="24" r="21" fill="none" stroke="#fff" stroke-width="2"/><path d="M19 15 L33 24 L19 33 Z" fill="#fff"/></svg></div>
      <div class="poster c3 r1" role="img" aria-label="Movie poster artwork, dim olive action scene" style="background:#3d3627"><svg class="play-icon" viewBox="0 0 48 48" aria-hidden="true"><circle cx="24" cy="24" r="21" fill="none" stroke="#fff" stroke-width="2"/><path d="M19 15 L33 24 L19 33 Z" fill="#fff"/></svg></div>
      <div class="poster c4 r1" role="img" aria-label="Movie poster artwork, light beige drama cover" style="background:#c8b39a"><svg class="play-icon" viewBox="0 0 48 48" aria-hidden="true"><circle cx="24" cy="24" r="21" fill="none" stroke="#fff" stroke-width="2"/><path d="M19 15 L33 24 L19 33 Z" fill="#fff"/></svg></div>

      <div class="poster c1 r2" role="img" aria-label="Movie poster artwork, warm golden night scene" style="background:#4e4128"><svg class="play-icon" viewBox="0 0 48 48" aria-hidden="true"><circle cx="24" cy="24" r="21" fill="none" stroke="#fff" stroke-width="2"/><path d="M19 15 L33 24 L19 33 Z" fill="#fff"/></svg></div>
      <div class="poster c2 r2" role="img" aria-label="Movie poster artwork, bold yellow action cover" style="background:#d2bb1f"><svg class="play-icon" viewBox="0 0 48 48" aria-hidden="true"><circle cx="24" cy="24" r="21" fill="none" stroke="#fff" stroke-width="2"/><path d="M19 15 L33 24 L19 33 Z" fill="#fff"/></svg></div>
      <div class="poster c3 r2" role="img" aria-label="Movie poster artwork, red and dark sci-fi cover" style="background:#6f2a1c"><svg class="play-icon" viewBox="0 0 48 48" aria-hidden="true"><circle cx="24" cy="24" r="21" fill="none" stroke="#fff" stroke-width="2"/><path d="M19 15 L33 24 L19 33 Z" fill="#fff"/></svg></div>
      <div class="poster c4 r2" role="img" aria-label="Movie poster artwork, warm ensemble comedy cover" style="background:#9a7a56"><svg class="play-icon" viewBox="0 0 48 48" aria-hidden="true"><circle cx="24" cy="24" r="21" fill="none" stroke="#fff" stroke-width="2"/><path d="M19 15 L33 24 L19 33 Z" fill="#fff"/></svg></div>

      <div class="poster c1 r3" role="img" aria-label="Movie poster artwork, colourful block-letter cover" style="background:#b9863a"><svg class="play-icon" viewBox="0 0 48 48" aria-hidden="true"><circle cx="24" cy="24" r="21" fill="none" stroke="#fff" stroke-width="2"/><path d="M19 15 L33 24 L19 33 Z" fill="#fff"/></svg></div>
      <div class="poster c2 r3" role="img" aria-label="Movie poster artwork, deep blue space scene" style="background:#27446f"><svg class="play-icon" viewBox="0 0 48 48" aria-hidden="true"><circle cx="24" cy="24" r="21" fill="none" stroke="#fff" stroke-width="2"/><path d="M19 15 L33 24 L19 33 Z" fill="#fff"/></svg></div>
      <div class="poster c3 r3" role="img" aria-label="Movie poster artwork, murky green horror cover" style="background:#3a4631"><svg class="play-icon" viewBox="0 0 48 48" aria-hidden="true"><circle cx="24" cy="24" r="21" fill="none" stroke="#fff" stroke-width="2"/><path d="M19 15 L33 24 L19 33 Z" fill="#fff"/></svg></div>
      <div class="poster c4 r3" role="img" aria-label="Movie poster artwork, pink heart-shaped collage" style="background:#c45a78"><svg class="play-icon" viewBox="0 0 48 48" aria-hidden="true"><circle cx="24" cy="24" r="21" fill="none" stroke="#fff" stroke-width="2"/><path d="M19 15 L33 24 L19 33 Z" fill="#fff"/></svg></div>
    </section>

  </main>
</body>
</html>
```